I'm looking for an app for customers to order through

I'm looking for an app for my customers to order products through
Ideally each customer would have a customer number with password
Their profile would come up with a preloaded products they currently order
From there they can select the product they require and volume needed for delivery
I would also like an option for them to go to a full product range if they are looking for Ideas or a product they don't currently use
Once the order is completed a copy of the order is them e-mailed to my distribution facilities and a confirmation sent to the customer by e-mail and/or SMS
Current product list is approx 1000 items
Current customers is 80 with expectations to expand to 200
On average current products ordered by each customer is is between 4-8 items
Ordering units are done by both weight and pieces/units

Target Market(s)

Food service outlets,
Restaurant , Hotels, catering companies, clubs, take away shops, cafes
Retail outlets

Number of Pages Required

1 page

Font styles to use
Sans Serif

Colors
abd037

Requirements
Must have
• Customer log in with Password 4 - 6 digit
• Customer order history
Nice to have
• Area for promotions / specials on a weekly / monthly basis

```html
<!DOCTYPE html>
<html lang="en">
<head>
<meta charset="utf-8">
<title>Customer Ordering App – Screens</title>
<link rel="stylesheet" href="https://fonts.googleapis.com/css2?family=Open+Sans:wght@400;600;700&display=swap">
<style>
  :root {
    --green: #abd037;
    --green-dark: #8fb327;
    --teal: #1f6b5e;
    --ink: #333a3f;
    --muted: #8a9096;
    --line: #e4e7ea;
    --screen: #ffffff;
    --backdrop: #dfe3e7;
    --field: #f4f5f6;
  }
  * { box-sizing: border-box; margin: 0; padding: 0; }
  html, body { width: 1200px; height: 1200px; overflow: hidden; }
  body {
    background: var(--backdrop);
    font-family: "Open Sans", sans-serif;
    color: var(--ink);
  }
  .board {
    width: 1200px; height: 1200px;
    display: grid;
    grid-template-columns: repeat(3, 360px);
    grid-template-rows: repeat(2, 560px);
    gap: 26px 30px;
    padding: 27px 30px;
  }
  .screen {
    background: var(--screen);
    position: relative;
    overflow: hidden;
    display: flex; flex-direction: column;
    box-shadow: 0 6px 18px rgba(0,0,0,.12);
  }
  .status-bar {
    background: var(--green); color: #fff;
    font-size: 10px; font-weight: 600;
    display: flex; justify-content: space-between;
    padding: 4px 10px 0;
    height: 20px;
  }
  .app-bar {
    background: var(--green); color: #fff;
    height: 40px; display: flex; align-items: center; justify-content: center;
    font-size: 15px; font-weight: 600; position: relative;
  }
  .app-bar .menu { position: absolute; left: 12px; top: 13px; }
  .content { flex: 1; overflow: hidden; }
  .photo { border-radius: 2px; }
  .photo-spread { background: linear-gradient(135deg, #6b3b22, #c9a27a); }
  .photo-steak { background: linear-gradient(135deg, #8e1e24, #d7636a); }
  .photo-box { background: linear-gradient(135deg, #c99a5d, #e8c897); }
  .photo-case { background: linear-gradient(135deg, #3c3f44, #9aa0a6); }
  .photo-snacks { background: linear-gradient(135deg, #2f6fb7, #e4453a 60%, #f3c431); }

  .tab-bar {
    height: 48px; border-top: 1px solid var(--line);
    display: flex; background: #fff;
  }
  .tab { flex: 1; display: flex; flex-direction: column; align-items: center; justify-content: center; font-size: 9px; color: var(--muted); gap: 2px; }
  .tab.active { color: var(--green-dark); }

  .product-grid { display: grid; grid-template-columns: 1fr 1fr; gap: 1px; background: var(--line); }
  .product-card { background: #fff; padding: 10px; height: 150px; display: flex; flex-direction: column; }
  .product-card .photo { height: 66px; margin-bottom: 6px; }
  .product-name { font-size: 9.5px; line-height: 1.3; color: var(--ink); height: 25px; overflow: hidden; }
  .product-foot { display: flex; justify-content: space-between; align-items: center; margin-top: auto; }
  .price { color: var(--green-dark); font-weight: 700; font-size: 11px; }
  .btn-small { background: var(--teal); color: #fff; font-size: 7.5px; font-weight: 700; padding: 3px 6px; letter-spacing: .3px; }

  .detail-top { position: relative; padding: 36px 20px 8px; text-align: center; }
  .close { position: absolute; left: 14px; top: 14px; }
  .detail-photo { height: 150px; margin: 0 40px; }
  .dots { display: flex; gap: 5px; justify-content: center; margin: 10px 0; }
  .dots span { width: 6px; height: 6px; border-radius: 50%; background: var(--line); }
  .dots span.on { background: var(--green); }
  .detail-title { font-size: 15px; font-weight: 600; padding: 0 20px; text-align: center; }
  .detail-price { text-align: center; color: var(--green-dark); font-size: 22px; font-weight: 700; margin-top: 6px; }
  .price-row { display: flex; justify-content: space-between; align-items: center; padding: 4px 20px 12px; border-bottom: 1px solid var(--line); }
  .original { font-size: 11px; color: var(--muted); }
  .original s { margin-left: 3px; }
  .save-badge { background: var(--green); color: #fff; font-size: 10px; font-weight: 600; padding: 3px 8px; }
  .section-label { font-size: 10px; color: var(--muted); letter-spacing: .6px; padding: 12px 20px 4px; text-transform: uppercase; }
  .details-text { font-size: 11.5px; line-height: 1.6; padding: 0 20px; color: var(--ink); }

  .login-body { padding: 60px 28px 0; }
  .brand { text-align: center; font-size: 22px; font-weight: 700; color: var(--green-dark); margin-bottom: 40px; display: flex; align-items: center; justify-content: center; gap: 8px; }
  .brand i { width: 14px; height: 14px; border-radius: 50%; background: var(--green); display: inline-block; }
  .field { border-bottom: 1px solid var(--line); padding: 10px 2px 8px; margin-bottom: 16px; }
  .field-label { font-size: 10px; color: var(--muted); text-transform: uppercase; letter-spacing: .5px; }
  .field-value { font-size: 14px; margin-top: 4px; letter-spacing: 1px; }
  .field-value.dots-pw { font-size: 18px; letter-spacing: 4px; line-height: 1; }
  .btn-wide { background: var(--green); color: #fff; text-align: center; font-size: 13px; font-weight: 600; letter-spacing: 1px; padding: 13px 0; text-transform: uppercase; }
  .login-body .btn-wide { margin-top: 22px; }
  .forgot { text-align: center; font-size: 11px; color: var(--muted); margin-top: 14px; }

  .cart-item { display: flex; gap: 12px; padding: 14px; border-bottom: 1px solid var(--line); position: relative; }
  .cart-item .photo { width: 70px; height: 60px; flex: none; }
  .cart-info { flex: 1; }
  .cart-info .product-name { font-size: 11px; height: auto; padding-right: 22px; }
  .cart-info .price { display: block; margin: 4px 0 6px; }
  .qty-row { display: flex; align-items: center; gap: 10px; font-size: 10px; color: var(--muted); }
  .stepper { display: flex; border: 1px solid var(--line); }
  .stepper span { width: 24px; height: 22px; display: flex; align-items: center; justify-content: center; font-size: 12px; color: var(--ink); }
  .stepper span + span { border-left: 1px solid var(--line); }
  .stepper .plus { color: var(--green-dark); }
  .trash { position: absolute; right: 14px; top: 14px; }
  .cart-spacer { flex: 1; }
  .cart-footer { margin-top: auto; }

  .summary { padding: 16px 20px; }
  .summary-row { display: flex; justify-content: space-between; font-size: 12px; padding: 6px 0; color: var(--ink); }
  .summary-row .label { color: var(--muted); }
  .summary-row.total { border-top: 1px solid var(--line); margin-top: 6px; padding-top: 10px; font-weight: 700; }
  .summary-row.total .amount { color: var(--green-dark); font-size: 15px; }
  .promo { display: flex; gap: 10px; align-items: flex-end; padding: 10px 20px; }
  .promo .field { flex: 1; margin: 0; }
  .btn-apply { background: var(--teal); color: #fff; font-size: 11px; font-weight: 700; padding: 8px 16px; letter-spacing: .5px; }
  .pay-spacer { flex: 1; }

  .order { display: flex; gap: 12px; padding: 14px; border-bottom: 1px solid var(--line); }
  .order .photo { width: 56px; height: 50px; flex: none; margin-top: 20px; }
  .order-store { font-size: 12px; font-weight: 700; }
  .order-address { font-size: 10px; color: var(--muted); margin-bottom: 6px; }
  .order-meta { display: grid; grid-template-columns: 70px 1fr; font-size: 10px; row-gap: 3px; }
  .order-meta dt { color: var(--muted); }
  .order-meta dd.id { color: var(--green-dark); font-weight: 600; }
  .order-meta dd.total { color: var(--green-dark); font-weight: 700; }
  .order .btn-small { display: inline-block; font-size: 9px; padding: 6px 14px; margin-top: 8px; }
</style>
</head>
<body>
<main class="board">

  <!-- Product list -->
  <section class="screen screen-products">
    <div class="status-bar"><span>●●●●● 3G</span><span>9:41 AM</span><span>100%</span></div>
    <header class="app-bar">
      <svg class="menu" width="16" height="12" viewBox="0 0 16 12"><path d="M0 1h16M0 6h16M0 11h16" stroke="#fff" stroke-width="2"/></svg>
      App Name
    </header>
    <div class="content">
      <div class="product-grid">
        <article class="product-card">
          <div class="photo photo-spread" role="img" aria-label="Jar of hazelnut cocoa spread"></div>
          <p class="product-name">Nocella Hazelnut Spread with Cocoa, 200g</p>
          <div class="product-foot"><span class="price">$24.48</span><span class="btn-small">ADD TO CART</span></div>
        </article>
        <article class="product-card">
          <div class="photo photo-case" role="img" aria-label="Three-compartment storage containers"></div>
          <p class="product-name">Sunvale Home Goods 3 Compartment Reusable</p>
          <div class="product-foot"><span class="price">$14.58</span><span class="btn-small">ADD TO CART</span></div>
        </article>
        <article class="product-card">
          <div class="photo photo-steak" role="img" aria-label="Raw rib eye steak"></div>
          <p class="product-name">Harlow Ridge Meats Aged 21 Oz Rib Eye Steak</p>
          <div class="product-foot"><span class="price">$70.81</span><span class="btn-small">ADD TO CART</span></div>
        </article>
        <article class="product-card">
          <div class="photo photo-case" role="img" aria-label="Three-compartment storage containers"></div>
          <p class="product-name">Sunvale Home Goods 3 Compartment Reusable</p>
          <div class="product-foot"><span class="price">$14.58</span><span class="btn-small">ADD TO CART</span></div>
        </article>
        <article class="product-card">
          <div class="photo photo-box" role="img" aria-label="Box of assorted grocery goods"></div>
          <p class="product-name">Sunvale Home Goods Pantry Box</p>
          <div class="product-foot"><span class="price">$345.50</span><span class="btn-small">ADD TO CART</span></div>
        </article>
        <article class="product-card">
          <div class="photo photo-snacks" role="img" aria-label="Assorted snack packs"></div>
          <p class="product-name">Assorted Snack Variety Pack</p>
          <div class="product-foot"><span class="price">$32.10</span><span class="btn-small">ADD TO CART</span></div>
        </article>
      </div>
    </div>
    <nav class="tab-bar">
      <div class="tab active"><svg width="18" height="16" viewBox="0 0 18 16"><path d="M2 8L9 2l7 6v7H11v-4H7v4H2z" fill="#8fb327"/></svg>Home</div>
      <div class="tab"><svg width="16" height="16" viewBox="0 0 16 16"><rect x="2" y="1" width="12" height="14" fill="none" stroke="#8a9096" stroke-width="1.5"/><path d="M5 5h6M5 8h6M5 11h4" stroke="#8a9096" stroke-width="1.5"/></svg>Order History</div>
      <div class="tab"><svg width="18" height="16" viewBox="0 0 18 16"><path d="M1 2h3l2 9h9l2-6H5" fill="none" stroke="#8a9096" stroke-width="1.5"/><circle cx="7" cy="14" r="1.3" fill="#8a9096"/><circle cx="14" cy="14" r="1.3" fill="#8a9096"/></svg>Cart</div>
    </nav>
  </section>

  <!-- Product detail -->
  <section class="screen screen-detail">
    <div class="detail-top">
      <svg class="close" width="12" height="12" viewBox="0 0 12 12"><path d="M1 1l10 10M11 1L1 11" stroke="#8a9096" stroke-width="1.6"/></svg>
      <div class="photo detail-photo photo-spread" role="img" aria-label="Jar of hazelnut cocoa spread"></div>
      <div class="dots"><span class="on"></span><span></span><span></span><span></span><span></span></div>
    </div>
    <h2 class="detail-title">Nocella Hazelnut Spread with Cocoa.</h2>
    <p class="detail-price">$24.48</p>
    <div class="price-row">
      <span class="original">Original: <s>$30.19</s></span>
      <span class="save-badge">You Save $5.71</span>
    </div>
    <p class="section-label">Details</p>
    <p class="details-text">Crisp golden wafers filled with a smooth hazelnut cocoa cream. Made with roasted hazelnuts, real cocoa and skimmed milk, with no artificial colours or preservatives. Perfect for breakfast, baking and snacks.</p>
  </section>

  <!-- Login -->
  <section class="screen screen-login">
    <div class="status-bar"><span>●●●●● 3G</span><span>9:41 AM</span><span>100%</span></div>
    <div class="login-body">
      <div class="brand"><i></i>App Name</div>
      <div class="field"><div class="field-label">Customer Number</div><div class="field-value">100482</div></div>
      <div class="field"><div class="field-label">Password</div><div class="field-value dots-pw">●●●●●●</div></div>
      <div class="btn-wide">Log In</div>
      <p class="forgot">Forgot password?</p>
    </div>
  </section>

  <!-- Cart -->
  <section class="screen screen-cart">
    <div class="status-bar"><span>●●●●● 3G</span><span>9:41 AM</span><span>100%</span></div>
    <header class="app-bar">
      <svg class="menu" width="16" height="12" viewBox="0 0 16 12"><path d="M0 1h16M0 6h16M0 11h16" stroke="#fff" stroke-width="2"/></svg>
      Cart (2)
    </header>
    <article class="cart-item">
      <div class="photo photo-spread" role="img" aria-label="Jar of hazelnut cocoa spread"></div>
      <div class="cart-info">
        <p class="product-name">Nocella Hazelnut Spread with Cocoa, 200g</p>
        <span class="price">$48.96</span>
        <div class="qty-row">Quantity <div class="stepper"><span>−</span><span>1</span><span class="plus">+</span></div></div>
      </div>
      <svg class="trash" width="14" height="16" viewBox="0 0 14 16"><path d="M1 3h12M5 3V1h4v2M2.5 3l1 12h7l1-12" fill="none" stroke="#8a9096" stroke-width="1.3"/></svg>
    </article>
    <article class="cart-item">
      <div class="photo photo-box" role="img" aria-label="Box of assorted grocery goods"></div>
      <div class="cart-info">
        <p class="product-name">Sunvale Home Goods 3 parts Compartment Reusable.</p>
        <span class="price">$345.50</span>
        <div class="qty-row">Quantity <div class="stepper"><span>−</span><span>1</span><span class="plus">+</span></div></div>
      </div>
      <svg class="trash" width="14" height="16" viewBox="0 0 14 16"><path d="M1 3h12M5 3V1h4v2M2.5 3l1 12h7l1-12" fill="none" stroke="#8a9096" stroke-width="1.3"/></svg>
    </article>
    <div class="cart-spacer"></div>
    <div class="cart-footer">
      <div class="btn-wide">Proceed to Checkout</div>
      <nav class="tab-bar">
        <div class="tab"><svg width="18" height="16" viewBox="0 0 18 16"><path d="M2 8L9 2l7 6v7H11v-4H7v4H2z" fill="none" stroke="#8a9096" stroke-width="1.5"/></svg>Home</div>
        <div class="tab"><svg width="16" height="16" viewBox="0 0 16 16"><rect x="2" y="1" width="12" height="14" fill="none" stroke="#8a9096" stroke-width="1.5"/><path d="M5 5h6M5 8h6M5 11h4" stroke="#8a9096" stroke-width="1.5"/></svg>Order History</div>
        <div class="tab active"><svg width="18" height="16" viewBox="0 0 18 16"><path d="M1 2h3l2 9h9l2-6H5" fill="none" stroke="#8fb327" stroke-width="1.5"/><circle cx="7" cy="14" r="1.3" fill="#8fb327"/><circle cx="14" cy="14" r="1.3" fill="#8fb327"/></svg>Cart</div>
      </nav>
    </div>
  </section>

  <!-- Checkout -->
  <section class="screen screen-checkout">
    <div class="status-bar"><span>●●●●● 3G</span><span>9:41 AM</span><span>100%</span></div>
    <header class="app-bar">
      <svg class="menu" width="16" height="12" viewBox="0 0 16 12"><path d="M0 1h16M0 6h16M0 11h16" stroke="#fff" stroke-width="2"/></svg>
      Checkout
    </header>
    <div class="summary">
      <div class="summary-row"><span class="label">Subtotal</span><span>$524.60</span></div>
      <div class="summary-row"><span class="label">Delivery</span><span>Free</span></div>
      <div class="summary-row"><span class="label">Tax</span><span>$25</span></div>
      <div class="summary-row"><span class="label">Packaging</span><span>$30</span></div>
      <div class="summary-row total"><span>Total</span><span class="amount">$579</span></div>
    </div>
    <div class="promo">
      <div class="field"><div class="field-label">Promotion Code</div><div class="field-value">&nbsp;</div></div>
      <span class="btn-apply">APPLY</span>
    </div>
    <div class="pay-spacer"></div>
    <div class="btn-wide">Pay with Credit Card</div>
  </section>

  <!-- Order history -->
  <section class="screen screen-history">
    <div class="status-bar"><span>●●●●● 3G</span><span>9:41 AM</span><span>100%</span></div>
    <header class="app-bar">
      <svg class="menu" width="16" height="12" viewBox="0 0 16 12"><path d="M0 1h16M0 6h16M0 11h16" stroke="#fff" stroke-width="2"/></svg>
      Order History
    </header>
    <div class="content">
      <article class="order">
        <div class="photo photo-spread" role="img" aria-label="Jar of hazelnut cocoa spread"></div>
        <div>
          <p class="order-store">Greenway Market,</p>
          <p class="order-address">18 Market Street, Riverside</p>
          <dl class="order-meta">
            <dt>Order ID</dt><dd class="id">#2368542</dd>
            <dt>Order Date</dt><dd>August 1,2016</dd>
            <dt>Status</dt><dd>Order Shipped</dd>
            <dt>Total Price</dt><dd class="total">$345.50</dd>
          </dl>
          <span class="btn-small">RE-ORDER</span>
        </div>
      </article>
      <article class="order">
        <div class="photo photo-steak" role="img" aria-label="Raw rib eye steak"></div>
        <div>
          <p class="order-store">Store Name,</p>
          <p class="order-address">412 Linden Court, Suite 6</p>
          <dl class="order-meta">
            <dt>Order ID</dt><dd class="id">#2368491</dd>
            <dt>Order Date</dt><dd>August 1,2016</dd>
            <dt>Status</dt><dd>Order Shipped</dd>
            <dt>Total Price</dt><dd class="total">$345.50</dd>
          </dl>
          <span class="btn-small">RE-ORDER</span>
        </div>
      </article>
    </div>
    <nav class="tab-bar">
      <div class="tab"><svg width="18" height="16" viewBox="0 0 18 16"><path d="M2 8L9 2l7 6v7H11v-4H7v4H2z" fill="none" stroke="#8a9096" stroke-width="1.5"/></svg>Home</div>
      <div class="tab active"><svg width="16" height="16" viewBox="0 0 16 16"><rect x="2" y="1" width="12" height="14" fill="#8fb327"/><path d="M5 5h6M5 8h6M5 11h4" stroke="#fff" stroke-width="1.5"/></svg>Order History</div>
      <div class="tab"><svg width="18" height="16" viewBox="0 0 18 16"><path d="M1 2h3l2 9h9l2-6H5" fill="none" stroke="#8a9096" stroke-width="1.5"/><circle cx="7" cy="14" r="1.3" fill="#8a9096"/><circle cx="14" cy="14" r="1.3" fill="#8a9096"/></svg>Cart</div>
    </nav>
  </section>

</main>
</body>
</html>
```